General Dental Office Business Card

I run a private general dental office in southern California, and would like a refresh/redesign of my business card. I focus on quality care rather than volume. The email address on the uploaded current card should be updated to: info@marbleshoredental.example. The current card's logo is a deboss, but I am open to other ideas. The logo can be refreshed, but it is something that's been with me since the beginning of the office, so I wouldn't want a drastic redesign.
Target Market(s)
Adults 18-99, whoever needs dental services
Industry/Entity Type
Healthcare/Dental
Contact Information for Business Card
Name, Address, Phone, email
Colors
Designer to choose colors to be used in the design.
Requirements
Must have
- Logo (Same as original one in the uploaded file), space on back for appointment time/date

```html
<!DOCTYPE html>
<html lang="en">
<head>
<meta charset="utf-8">
<title>Marble Shore Dental – Business Card</title>
<link rel="stylesheet" href="https://fonts.googleapis.com/css2?family=Outfit:wght@300;400;600;700&display=swap">
<style>
  :root {
    --bg-dark: #dfe2e3;
    --bg-light: #efefef;
    --teal: #2eb5c3;
    --teal-deep: #2aacba;
    --teal-soft: #5cc8d4;
    --pale: #effaf8;
    --white: #ffffff;
    --sea-top: #60c3d3;
    --sea-mid: #6ad0e1;
    --sea-bottom: #7ce5f4;
  }
  * { margin: 0; padding: 0; box-sizing: border-box; }
  html, body { width: 1200px; height: 1200px; overflow: hidden; }
  body {
    position: relative;
    background: var(--bg-dark);
    font-family: "Outfit", sans-serif;
  }
  .backdrop-split { position: absolute; inset: 0; width: 1200px; height: 1200px; }

  .card {
    position: absolute;
    width: 301px;
    height: 525px;
    overflow: hidden;
    text-align: center;
  }
  .card--rounded { border-radius: 31px; }
  .row-top { top: 59px; }
  .row-bottom { top: 616px; }
  .col-left { left: 288px; }
  .col-right { left: 611px; }

  .card-front { background: var(--teal); color: var(--white); }
  .card-back { background: var(--pale); color: var(--teal); }

  .dentist-name {
    position: absolute; top: 43px; left: 0; right: 0;
    font-weight: 700; font-size: 23px; letter-spacing: 0.5px; line-height: 1;
  }
  .dentist-title {
    position: absolute; top: 70px; left: 0; right: 0;
    font-weight: 400; font-size: 14px; letter-spacing: 1px; line-height: 1;
  }
  .brand-mark {
    position: absolute; left: 50%;
    border-radius: 50%;
    transform: translateX(-50%);
  }
  .card-front .brand-mark {
    top: 123px; width: 92px; height: 92px;
    border: 4px solid var(--white);
  }
  .card-back .brand-mark {
    top: 150px; width: 108px; height: 108px;
    border: 5px solid var(--teal);
  }
  .brand-name {
    position: absolute; left: 0; right: 0;
    font-weight: 400; line-height: 1.05;
  }
  .card-front .brand-name { top: 245px; font-size: 23px; }
  .card-back .brand-name { top: 292px; font-size: 28px; }

  .contact-list {
    position: absolute; top: 323px; left: 0; right: 0;
    list-style: none; font-weight: 300; font-size: 15px; line-height: 20px;
  }
  .contact-list .phone { margin: 2px 0; }

  .appointment-field {
    position: absolute; left: 29px; right: 28px;
    font-size: 13.5px; font-weight: 300; text-align: left;
    border-bottom: 1px solid var(--teal);
    padding-bottom: 1px; line-height: 1;
  }
  .appointment-field--date { top: 27px; }
  .appointment-field--time { top: 57px; }

  .sea-band { position: absolute; left: 0; right: 0; bottom: 0; }
  .card-front .sea-band {
    height: 110px;
    background: linear-gradient(to bottom,
      rgba(92, 200, 212, 0) 0%,
      var(--teal-soft) 22%,
      #45bdca 60%,
      var(--teal-deep) 100%);
  }
  .card-back .sea-band {
    height: 102px;
    background: linear-gradient(to bottom,
      var(--sea-top) 0%,
      var(--sea-mid) 50%,
      var(--sea-bottom) 100%);
  }
</style>
</head>
<body>
  <svg class="backdrop-split" viewBox="0 0 1200 1200" aria-hidden="true">
    <polygon points="1200,0 1200,1200 0,1200" fill="var(--bg-light)"/>
  </svg>

  <!-- Front, square corners -->
  <section class="card card-front row-top col-left">
    <h1 class="dentist-name">ELENA R. MARSH DDS</h1>
    <p class="dentist-title">GENERAL DENTISTRY</p>
    <div class="brand-mark" aria-hidden="true"></div>
    <p class="brand-name">MARBLE SHORE<br>DENTAL</p>
    <ul class="contact-list">
      <li>1280 Harborview Lane</li>
      <li>Seacliff, CA 90000</li>
      <li class="phone">555-014-2760</li>
      <li>info@marbleshoredental.example</li>
      <li>www.marbleshoredental.example</li>
    </ul>
    <div class="sea-band" role="img" aria-label="Layered water waves decoration"></div>
  </section>

  <!-- Back, square corners -->
  <section class="card card-back row-top col-right">
    <p class="appointment-field appointment-field--date">Appointment Date:</p>
    <p class="appointment-field appointment-field--time">Time:</p>
    <div class="brand-mark" aria-hidden="true"></div>
    <p class="brand-name">MARBLE SHORE<br>DENTAL</p>
    <div class="sea-band" role="img" aria-label="Layered water waves decoration"></div>
  </section>

  <!-- Front, rounded corners -->
  <section class="card card--rounded card-front row-bottom col-left">
    <h1 class="dentist-name">ELENA R. MARSH DDS</h1>
    <p class="dentist-title">GENERAL DENTISTRY</p>
    <div class="brand-mark" aria-hidden="true"></div>
    <p class="brand-name">MARBLE SHORE<br>DENTAL</p>
    <ul class="contact-list">
      <li>1280 Harborview Lane</li>
      <li>Seacliff, CA 90000</li>
      <li class="phone">555-014-2760</li>
      <li>info@marbleshoredental.example</li>
      <li>www.marbleshoredental.example</li>
    </ul>
    <div class="sea-band" role="img" aria-label="Layered water waves decoration"></div>
  </section>

  <!-- Back, rounded corners -->
  <section class="card card--rounded card-back row-bottom col-right">
    <p class="appointment-field appointment-field--date">Appointment Date:</p>
    <p class="appointment-field appointment-field--time">Time:</p>
    <div class="brand-mark" aria-hidden="true"></div>
    <p class="brand-name">MARBLE SHORE<br>DENTAL</p>
    <div class="sea-band" role="img" aria-label="Layered water waves decoration"></div>
  </section>
</body>
</html>
```